The Corvane Agency

We are a pr, social media and strategy agency specializing in the pet industry. We would like a new dynamic design of our existing website. We think it is currently outdated and looks too corporate. We would like it to look more consumer oriented as we primarily market pet products. We would like warm imagery involving pets and while pets are fun, this is still a business website and needs to maintain a professional look. We are hired by business owners and executives.
I would like some of our work featured on the home page.
Our primary service tabs are:
Public Relations
Social Media
Product Consulting
Most of the content will remain the same but we are open to suggestions!
Our current website can be found at www.corvanepetpr.example.
We are open to other colors than in our logo and on our current page.
This is a design only project and will not require programming. The selected designer will need to provide at least one interior page in addition to the home page.

Industry/Entity Type

Pet

Requirements
Should not have
• Cartoon type figures. Pet puns.

```html
<!DOCTYPE html>
<html lang="en">
<head>
<meta charset="utf-8">
<title>The Corvane Agency</title>
<link href="https://fonts.googleapis.com/css2?family=PT+Sans:wght@400;700&family=PT+Sans+Narrow:wght@700&family=Open+Sans:wght@300&display=swap" rel="stylesheet">
<style>
:root{
  --red:#d7261e;
  --orange:#e0662a;
  --link:#d86a0d;
  --ink:#2b2b2b;
  --body:#5a5a5a;
  --muted:#8a8a8a;
  --page:#f4f4f4;
  --line:#d6d6d6;
  --white:#ffffff;
}
*{margin:0;padding:0;box-sizing:border-box}
html,body{width:1049px;height:1200px;overflow:hidden}
body{position:relative;background:var(--page);font-family:"PT Sans",Arial,sans-serif;color:var(--ink)}
.abs{position:absolute}
.top-rule{left:0;top:4px;width:1049px;height:4px;background:linear-gradient(#e2e2e2,#f4f4f4)}
.brand-tab{left:108px;top:0;width:216px;height:112px;background:var(--white);border-radius:0 0 110px 110px/0 0 60px 60px;box-shadow:0 4px 10px rgba(0,0,0,.12)}
.brand-name{left:108px;top:30px;width:216px;text-align:center;font-size:22px;font-weight:700;color:var(--red);line-height:1}
.brand-name small{display:block;font-size:14px;margin-top:4px}
.phone{left:790px;top:15px;display:flex;align-items:center;gap:8px;font-size:16px;font-weight:700;letter-spacing:.5px}
.nav{left:390px;top:51px;width:526px;height:40px;background:linear-gradient(#fdfdfd,#ececec);border:1px solid var(--line);border-radius:6px;display:flex;align-items:center;padding-left:18px}
.nav a{flex:none;font-size:13px;color:#555;text-decoration:none;white-space:nowrap;text-align:center;height:38px;line-height:38px;border-right:1px solid var(--line)}
.nav a:last-child{border-right:0}
.nav .current{background:linear-gradient(#d8332a,#b51a13);color:var(--white);font-weight:700;height:50px;margin-top:-12px;line-height:46px;border-radius:2px 2px 6px 6px;border-right:0}
.slider{left:133px;top:119px;width:783px;height:353px;border:1px solid var(--line);background:var(--white);padding:7px}
.slide{width:100%;height:100%;border:1px solid #e3e3e3;position:relative;background:var(--white)}
.slide-copy{z-index:2}
.slide-title{left:25px;top:84px;font-family:"PT Sans Narrow",sans-serif;font-weight:700;font-size:48px;color:#555;line-height:1;white-space:nowrap}
.slide-sub{left:48px;top:132px;font-family:"Open Sans",sans-serif;font-weight:300;font-size:48px;color:#666;line-height:1;white-space:nowrap}
.slide-text{left:48px;top:200px;width:280px;font-size:12px;line-height:15px;color:var(--body)}
.slide-link{left:48px;top:270px;font-size:14px;font-weight:700;color:var(--link)}
.slide-photo{left:345px;top:30px;width:420px;height:300px;border-radius:6px;background:radial-gradient(ellipse at 55% 60%,#d9d3cc 0%,#eee9e4 55%,#ffffff 78%)}
.arrow-btn{width:30px;height:66px;background:linear-gradient(90deg,#cfcfcf,#9d9d9d);display:flex;align-items:center;justify-content:center}
.arrow-prev{left:118px;top:262px;border-radius:33px 0 0 33px}
.arrow-next{left:902px;top:262px;border-radius:0 33px 33px 0}
.section-title{font-size:23px;font-weight:400;color:var(--ink);line-height:1;white-space:nowrap}
.section-title span{color:var(--red)}
.welcome-text{left:136px;top:514px;width:488px;font-size:12px;line-height:14.6px;color:var(--body);text-align:justify}
.more{left:576px;top:621px;font-size:12px;font-weight:700;color:var(--link)}
.team-photo{left:660px;top:515px;width:243px;height:120px;border:3px solid var(--white);box-shadow:0 0 0 1px var(--line);background:linear-gradient(90deg,#3d3436,#b39b8e 50%,#3a3234)}
.dash-h{left:134px;top:648px;width:781px;border-top:1px dashed #c9c9c9}
.services-shadow{left:624px;top:676px;width:10px;height:200px;background:linear-gradient(90deg,rgba(0,0,0,.1),transparent)}
.service{width:160px;text-align:center}
.service-ring{width:88px;height:88px;margin:0 auto;border-radius:50%;background:linear-gradient(#ffffff,#e6e6e6);box-shadow:0 3px 6px rgba(0,0,0,.18),inset 0 0 0 5px #f7f7f7;display:flex;align-items:center;justify-content:center}
.service-label{margin-top:16px;font-size:15px;color:var(--red);white-space:nowrap}
.testimonial-photo{left:660px;top:734px;width:86px;height:89px;border:3px solid var(--white);box-shadow:0 0 0 1px var(--line);background:linear-gradient(#b08a63,#e7c8ad)}
.quote{left:752px;top:735px;width:152px;font-size:11.5px;line-height:13.5px;color:#444}
.quote-mark{font-family:Georgia,serif;font-size:30px;color:#999;line-height:0;vertical-align:-10px}
.quote-name{left:754px;top:798px;font-size:12.5px;color:var(--red)}
.quote-company{left:754px;top:815px;font-size:12.5px;font-weight:700;color:var(--ink)}
.shadow-h{left:134px;top:884px;width:781px;height:6px;background:radial-gradient(ellipse at center top,rgba(0,0,0,.12),transparent 70%)}
.post-img{height:112px;border:3px solid var(--white);box-shadow:0 0 0 1px var(--line)}
.post-title{font-size:12.5px;line-height:15px;color:var(--red)}
.post-title.single{white-space:nowrap}
.post-date{font-size:12.5px;color:var(--ink)}
.post-text{font-size:12px;line-height:14.5px;color:var(--muted)}
.dash-v{left:524px;top:934px;height:118px;border-left:1px dashed #c9c9c9}
.footer{left:0;top:1072px;width:1049px;height:128px;background:var(--orange);color:var(--white);text-align:center;font-size:12.5px}
.footer-links{margin-top:6px;display:flex;justify-content:center;gap:16px}
.footer-links span{opacity:.9}
.footer-row{margin-top:7px;display:flex;justify-content:center;align-items:center;gap:6px}
.social{width:17px;height:17px;border-radius:2px;background:var(--white)}
</style>
</head>
<body>
<div class="abs top-rule"></div>
<div class="abs brand-tab"></div>
<div class="abs brand-name">The Corvane<small>Agency</small></div>

<div class="abs phone">
  <svg width="20" height="20" viewBox="0 0 20 20"><circle cx="10" cy="10" r="9" fill="none" stroke="#d7261e" stroke-width="1.6"/><path d="M7 5.5l2 2-1 1.2c.6 1.3 1.6 2.3 2.9 2.9l1.2-1 2 2-1.2 1.4C10 13.8 6.2 10 6 6.6z" fill="#d7261e"/></svg>
  555.014.2290
</div>

<nav class="abs nav">
  <a class="current" href="#" style="width:57px">Home</a>
  <a href="#" style="width:117px">Public Relations</a>
  <a href="#" style="width:91px">Social Media</a>
  <a href="#" style="width:86px">Pet Experts</a>
  <a href="#" style="width:155px">Business Development</a>
</nav>

<div class="abs slider">
  <div class="slide">
    <div class="abs slide-photo" role="img" aria-label="Group of pets: a spotted dog, cats, parrot, puppy, rabbit, ferret and goldfish bowl"></div>
    <div class="abs slide-title slide-copy">Redefining</div>
    <div class="abs slide-sub slide-copy">pet Services</div>
    <p class="abs slide-text slide-copy">No other agency matches our pet industry experience, period. From serving on industry boards to managing media at trade shows, helping to grow associations.</p>
    <div class="abs slide-link slide-copy">Read more</div>
  </div>
</div>
<div class="abs arrow-btn arrow-prev"><svg width="14" height="24" viewBox="0 0 14 24"><path d="M11 2L3 12l8 10" fill="none" stroke="#555" stroke-width="3"/></svg></div>
<div class="abs arrow-btn arrow-next"><svg width="14" height="24" viewBox="0 0 14 24"><path d="M3 2l8 10-8 10" fill="none" stroke="#555" stroke-width="3"/></svg></div>

<h2 class="abs section-title" style="left:136px;top:483px">Welcome to <span>Corvane</span></h2>
<p class="abs welcome-text">PR has evolved from public relations to personal relations. As new communication tools have emerged, old habits have been buried, giving way to the consumer revolution of social media. At Corvane, we tap the best ways to connect you with those in the pet industry. That focus makes our team your ideal partner for creating a community as faithful as a favorite pet. There really was no other name in the world that was a better fit. Our name stands for the people and pets who together define who we are.</p>
<div class="abs more">more [+]</div>

<h2 class="abs section-title" style="left:659px;top:484px">Our <span>Team</span></h2>
<div class="abs team-photo" role="img" aria-label="Agency team standing together in a row"></div>

<div class="abs dash-h"></div>

<h2 class="abs section-title" style="left:135px;top:673px">Our <span>Services</span></h2>
<div class="abs services-shadow"></div>
<div class="abs service" style="left:119px;top:735px">
  <div class="service-ring"><svg width="44" height="40" viewBox="0 0 44 40"><path d="M6 16h8l16-10v28L14 24H6z" fill="#555"/><path d="M10 24l4 12h5l-3-12z" fill="#555"/><path d="M35 12c3 3 3 9 0 12M38 8c5 5 5 15 0 20" fill="none" stroke="#555" stroke-width="2"/></svg></div>
  <div class="service-label">Public Relations</div>
</div>
<div class="abs service" style="left:273px;top:735px">
  <div class="service-ring"><svg width="42" height="38" viewBox="0 0 42 38"><rect x="2" y="4" width="38" height="24" rx="4" fill="#555"/><path d="M10 28l-2 8 10-8z" fill="#555"/><circle cx="13" cy="16" r="2.5" fill="#fff"/><circle cx="21" cy="16" r="2.5" fill="#fff"/><circle cx="29" cy="16" r="2.5" fill="#fff"/></svg></div>
  <div class="service-label">Social Media</div>
</div>
<div class="abs service" style="left:433px;top:735px">
  <div class="service-ring"><svg width="36" height="40" viewBox="0 0 36 40"><circle cx="18" cy="12" r="9" fill="#555"/><path d="M2 38c0-10 7-15 16-15s16 5 16 15z" fill="#555"/></svg></div>
  <div class="service-label">Product Consulting</div>
</div>

<h2 class="abs section-title" style="left:659px;top:673px">Client <span>Testimonials</span></h2>
<svg class="abs" style="left:690px;top:711px" width="28" height="16" viewBox="0 0 28 16"><path d="M2 14L14 3l12 11" fill="none" stroke="#aaa" stroke-width="3"/></svg>
<div class="abs testimonial-photo" role="img" aria-label="Portrait of client director"></div>
<p class="abs quote"><span class="quote-mark">“</span> Lorem ipsum dolor sit Lorem fdaafipsum dafsdolor sit amet, consectetuer adipiscing elit, sed diam <span class="quote-mark">”</span></p>
<div class="abs quote-name">Marla [Director]</div>
<div class="abs quote-company">XYZ Company</div>
<svg class="abs" style="left:690px;top:832px" width="28" height="16" viewBox="0 0 28 16"><path d="M2 2l12 11L26 2" fill="none" stroke="#aaa" stroke-width="3"/></svg>

<div class="abs shadow-h"></div>

<h2 class="abs section-title" style="left:135px;top:900px">Our <span>Blog</span></h2>
<svg class="abs" style="left:232px;top:903px" width="40" height="20" viewBox="0 0 40 20"><path d="M10 2L3 10l7 8M28 2l7 8-7 8" fill="none" stroke="#999" stroke-width="3"/></svg>

<div class="abs post-img" style="left:143px;top:939px;width:190px;background:linear-gradient(90deg,#3b5c86,#7a6652 50%,#c8b49a)" role="img" aria-label="Guest presenting a product on a morning television show"></div>
<div class="abs post-title single" style="left:338px;top:939px">Bramwell Featured on Day Talk</div>
<div class="abs post-date" style="left:338px;top:961px">Jan 3rd, 2014</div>
<p class="abs post-text" style="left:338px;top:981px;width:180px">Our client was featured with pet expert Dalton Reeve on Day Talk as part of a . Great job Dalton, but the Auto Grass and Booster Seat made the segment</p>

<div class="abs dash-v"></div>

<div class="abs post-img" style="left:536px;top:939px;width:190px;background:radial-gradient(circle at 50% 60%,#6b7f95,#d6d6d6 60%,#f4f4f4)" role="img" aria-label="Sketch of a head with speech bubbles representing brainstorming"></div>
<div class="abs post-title" style="left:730px;top:939px;width:180px">The Evolution of the Ideas: Brainstorming</div>
<div class="abs post-date" style="left:730px;top:977px">August 13th, 2013</div>
<p class="abs post-text" style="left:730px;top:997px;width:168px;text-align:justify">As someone who was in the service industry for years, collaborating on creative ideas and bouncing them off of others</p>

<footer class="abs footer">
  <div class="footer-links"><span>Contact</span><span>|</span><span>Careers</span><span>|</span><span>Love List</span><span>|</span><span>Blog</span><span>|</span><span>Sitemap</span></div>
  <div class="footer-row"><svg width="12" height="14" viewBox="0 0 12 14"><path d="M6 1a4.5 4.5 0 0 0-4.5 4.5C1.5 9 6 13 6 13s4.5-4 4.5-7.5A4.5 4.5 0 0 0 6 1z" fill="#fff"/><circle cx="6" cy="5.5" r="1.6" fill="#e0662a"/></svg>48 Alder Crest Dr. NV 89000</div>
  <div class="footer-row"><svg width="14" height="14" viewBox="0 0 20 20"><circle cx="10" cy="10" r="9" fill="none" stroke="#fff" stroke-width="1.8"/><path d="M7 5.5l2 2-1 1.2c.6 1.3 1.6 2.3 2.9 2.9l1.2-1 2 2-1.2 1.4C10 13.8 6.2 10 6 6.6z" fill="#fff"/></svg>555.014.2290</div>
  <div class="footer-row" style="gap:10px"><span class="social"></span><span class="social"></span><span class="social"></span></div>
  <div class="footer-row">©2014 The Corvane Agency</div>
</footer>
</body>
</html>
```